依頼詳細
販売商品は下記の3種類です。詳細はURLをご参照下さい。

1.工業用精製水 (用途:実験室などでの試験器具洗浄など)
http://www.hanabo-tenko.com/shop/goods/goods/goods.php?act=Goods&mode=Detail&id=00054986

2.バッテリー補充液 (用途:バッテリーの補充液など)
http://www.hanabo-tenko.com/shop/goods/goods/goods.php?act=Goods&mode=Detail&id=00054987

3.高純度精製水 (用途:エステスチーマーや加湿器の補給水など)
http://www.hanabo-tenko.com/shop/goods/goods/goods.php?act=Goods&mode=Detail&id=00066908

精製水は純度の高い水(きれいな水)ですので、商品に相応しい爽やかな印象を持っていただけるデザインを希望します。全体的にブルー系統のカラーを希望します。

添付の原案のレイアウト通りの必要はありません。見やすく目的に沿った内容であれば、画像等の追加、文章やフレーズ、フォント、文字サイズなどの修正、加筆もOKです。基本的にはデザインを重視したいと思います。

記載事項が多いので、A4サイズに収まるレイアウトの工夫をお願い致します。
記載項目
添付の【原案】をご参照下さい。
サイズ
A4
ページ数
両面
希望イメージ
シンプル 複雑
単色 カラフル
暗い 明るい
日常 高級
遊び心 厳粛
未来的 伝統的
女性的 男性的
希望する色
水色系
納品ファイル
• 高解像度JPG (.jpg)
• イラストレーター形式 (.ai)
補足説明

当社の要望・イメージに最も近いデザインでした。

みなさん非常に素晴らしいご提案でしたので、選定に苦慮いたしました。

選定できなかった皆様には申し訳ございませんでしたが、またの機会がございましたらよろしくお願い致します。皆様のご尽力にとても感謝致します。

この度は誠にありがとうございました。

```html
<!DOCTYPE html>
<html lang="ja">
<head>
<meta charset="utf-8">
<title>精製水のご案内</title>
<link href="https://fonts.googleapis.com/css2?family=Noto+Sans+JP:wght@400;500;700;900&family=M+PLUS+Rounded+1c:wght@700;800&family=Great+Vibes&display=swap" rel="stylesheet">
<style>
:root{
  --blue:#1a86d0;
  --blue-dark:#0b4f8f;
  --navy:#173a63;
  --sky:#dff1fb;
  --sky-mid:#b9e0f5;
  --red:#e0262b;
  --ink:#2b2b2b;
  --line:#9ccbe8;
  --white:#fff;
}
*{box-sizing:border-box;margin:0;padding:0}
html,body{width:878px;height:1200px;overflow:hidden;background:var(--white)}
body{font-family:"Noto Sans JP",sans-serif;color:var(--ink);position:relative}
.sheet{position:absolute;inset:0;background:linear-gradient(180deg,#eaf6fd 0,#fff 260px)}
.title{position:absolute;left:28px;top:14px;font-family:"M PLUS Rounded 1c",sans-serif;font-weight:800;font-size:66px;color:var(--blue);letter-spacing:2px;text-shadow:3px 3px 0 #fff}
.title-en{position:absolute;right:30px;top:18px;font-family:"Great Vibes",cursive;font-size:44px;line-height:40px;color:var(--blue);text-align:right}
.same-day{position:absolute;left:30px;top:100px;font-weight:900;font-size:32px;color:var(--blue-dark)}
.same-day em{font-style:normal;color:var(--red)}
.same-day-note{position:absolute;left:432px;top:104px;width:420px;height:34px;background:var(--navy);color:var(--white);font-size:15px;font-weight:700;display:flex;align-items:center;justify-content:center;border-radius:3px}
.features{position:absolute;left:24px;top:150px;width:830px;height:92px;display:flex;align-items:center;gap:16px}
.badge{width:86px;height:86px;border-radius:50%;background:var(--red);color:#fff;font-weight:900;font-size:19px;line-height:22px;display:flex;align-items:center;justify-content:center;text-align:center;flex:none}
.feature-list{list-style:none;font-size:13.5px;line-height:24px;color:var(--navy)}
.feature-list li::before{content:"●";color:var(--blue);margin-right:6px}
.lineup{position:absolute;left:24px;top:252px;width:620px;height:46px;background:var(--blue);color:#fff;font-weight:900;font-size:21px;display:flex;align-items:center;padding-left:18px;border-radius:4px}
.cock{position:absolute;left:24px;top:310px;font-size:17px;font-weight:700;color:var(--navy)}
.cock small{font-size:11px;font-weight:400}
.cock-photo{position:absolute;left:660px;top:246px;width:194px;height:88px;border-radius:6px;background:radial-gradient(circle at 50% 55%,#c9ccd1,#7d848d)}
.products{position:absolute;left:24px;top:344px;width:830px;display:grid;grid-template-columns:repeat(3,1fr);gap:14px}
.product-photo{height:144px;border-radius:4px;background:linear-gradient(160deg,#ffffff,#cfe3f0)}
.product:nth-child(2) .product-photo{background:linear-gradient(160deg,#fff4d6,#f1b64a)}
.product:nth-child(3) .product-photo{background:linear-gradient(160deg,#ffffff,#d8e4ea)}
.product-name{margin-top:6px;display:flex;align-items:center;gap:6px;font-weight:900;font-size:16px;color:var(--blue-dark);border-left:6px solid var(--blue);padding-left:6px}
.product-name span{font-size:11px;color:#fff;background:var(--blue);padding:1px 5px;border-radius:2px}
.product-desc{font-size:11.5px;line-height:17px;margin-top:5px}
.spec{position:absolute;left:24px;top:572px;width:830px;border-collapse:collapse;font-size:12px}
.spec th,.spec td{border:1px solid var(--line);padding:4px 8px}
.spec th{background:var(--sky-mid);color:var(--navy);width:80px}
.price{position:absolute;left:24px;top:622px;width:830px;height:66px;background:var(--sky);border-top:3px solid var(--blue);border-bottom:3px solid var(--blue)}
.price-lead{position:absolute;left:16px;top:6px;font-weight:900;font-size:20px;color:var(--blue-dark)}
.price-sub{position:absolute;left:16px;top:36px;font-weight:700;font-size:16px;color:var(--red)}
.price-value{position:absolute;right:16px;top:2px;font-weight:900;font-size:48px;line-height:60px;color:var(--red)}
.price-value small{font-size:14px;color:var(--ink)}
.price-value i{font-style:normal;font-size:22px}
.purchase{position:absolute;left:24px;top:704px;width:490px}
.section-head{font-weight:700;font-size:14px;color:var(--navy);border-bottom:2px solid var(--blue);padding-bottom:4px;margin-bottom:12px}
.route{display:flex;align-items:flex-start;gap:10px;margin-bottom:20px}
.route-label{flex:none;width:104px;height:28px;background:var(--blue);color:#fff;font-weight:700;font-size:14px;display:flex;align-items:center;justify-content:center;border-radius:3px}
.route-body{font-size:13px;line-height:20px}
.search{display:flex;border:2px solid var(--blue);width:220px;height:28px;margin-bottom:4px}
.search div{flex:1;font-size:13px;padding:3px 8px}
.search b{width:50px;background:var(--blue);color:#fff;font-size:12px;display:flex;align-items:center;justify-content:center}
.shops{list-style:none;columns:2;column-gap:18px;font-size:12.5px;line-height:21px}
.shops li::before{content:"・"}
.tel{font-weight:900;font-size:26px;color:var(--blue-dark);line-height:28px}
.tel small{display:block;font-size:11px;font-weight:400;color:var(--ink);line-height:15px}
.mail{font-weight:700;font-size:20px;color:var(--blue-dark);line-height:28px}
.oem{position:absolute;left:530px;top:704px;width:324px;height:364px;background:var(--sky);border-radius:8px;padding:16px}
.oem-title{font-weight:900;font-size:19px;line-height:28px;color:var(--blue-dark)}
.oem-badge{position:absolute;right:14px;top:74px;width:82px;height:82px;border-radius:50%;background:var(--red);color:#fff;font-weight:900;font-size:14px;line-height:18px;display:flex;align-items:center;justify-content:center;text-align:center}
.oem-text{margin-top:16px;width:200px;font-size:12px;line-height:19px}
.oem-points{margin-top:18px;background:#fff;border:2px solid var(--blue);border-radius:6px;padding:10px 12px;list-style:none;font-size:12px;line-height:20px;color:var(--navy);font-weight:700}
.oem-points li::before{content:"✔ ";color:var(--red)}
.contact{position:absolute;left:24px;top:1084px;width:830px;height:48px;border:2px solid var(--blue);border-radius:4px;display:flex;align-items:center;gap:16px;padding:0 14px}
.contact-tag{background:var(--navy);color:#fff;font-size:12px;font-weight:700;padding:4px 8px}
.company{font-weight:700;font-size:15px}
.company small{font-size:11px;font-weight:400}
.contact-num{margin-left:auto;font-weight:900;font-size:22px;color:var(--blue-dark);display:flex;gap:18px}
.contact-num span small{font-size:12px;margin-right:4px}
.fax-band{position:absolute;left:0;top:1144px;width:878px;height:56px;background:var(--blue);color:#fff;font-weight:900;font-size:22px;display:flex;align-items:center;justify-content:center}
.fax-band b{color:#fff36b}
</style>
</head>
<body>
<div class="sheet">
  <h1 class="title">精製水のご案内</h1>
  <div class="title-en">Purified<br>water</div>

  <p class="same-day"><em>16時</em>までは当日出荷!</p>
  <p class="same-day-note">16時以降及び休業日は翌営業日の出荷となります。</p>

  <section class="features">
    <div class="badge">商品<br>特徴</div>
    <ul class="feature-list">
      <li>逆浸透膜とイオン交換樹脂で精製した、純度の高い精製水です。</li>
      <li>自社工場で製造・充填し、品質管理を徹底してお届けしています。</li>
      <li>衛生的な箱入りパックで、保管や持ち運びにも便利です。</li>
    </ul>
  </section>

  <div class="lineup">用途に応じて3種類の精製水をご用意しております!</div>
  <p class="cock">抽出に便利なコック付き! <small>(内袋の外に取り付け可能)</small></p>
  <div class="cock-photo" role="img" aria-label="箱に取り付けた抽出用コックの写真"></div>

  <section class="products">
    <article class="product">
      <div class="product-photo" role="img" aria-label="工業用精製水の箱の写真"></div>
      <h2 class="product-name">工業用精製水<span>AQ-01</span></h2>
      <p class="product-desc">実験室などでの試験器具の洗浄や、各種工業用途にお使いいただけます。</p>
    </article>
    <article class="product">
      <div class="product-photo" role="img" aria-label="バッテリー補充液の箱の写真"></div>
      <h2 class="product-name">バッテリー補充液<span>AQ-02</span></h2>
      <p class="product-desc">バッテリーの補充液として、フォークリフトや車両の整備にご利用ください。</p>
    </article>
    <article class="product">
      <div class="product-photo" role="img" aria-label="高純度精製水の箱の写真"></div>
      <h2 class="product-name">高純度精製水<span>AQ-03</span></h2>
      <p class="product-desc">エステスチーマーや加湿器の補給水など、より高い純度が必要な用途に。</p>
    </article>
  </section>

  <table class="spec">
    <tr><th>容量</th><td>20L</td><th>サイズ</th><td>200×300×300mm</td><th>重量</th><td>約21kg</td></tr>
  </table>

  <section class="price">
    <p class="price-lead">自社製造、直販だからできる納得の価格!</p>
    <p class="price-sub">まとめ買いの場合、さらに割安となります。</p>
    <p class="price-value"><small>(税込)</small>945<i>円~</i></p>
  </section>

  <section class="purchase">
    <h3 class="section-head">ご購入は、下記のいずれかの方法でお願いします。</h3>
    <div class="route">
      <div class="route-label">インターネット</div>
      <div class="route-body">
        <div class="search"><div>精製水</div><b>検索</b></div>
        <ul class="shops">
          <li>アクア通販</li>
          <li>アクア通販 本店</li>
          <li>モールA店</li>
          <li>アクアネット</li>
          <li>モールB店</li>
        </ul>
      </div>
    </div>
    <div class="route">
      <div class="route-label">お電話</div>
      <p class="tel">0120-000-111<small>受付時間 平日 9:00~17:00(土日祝を除く)</small></p>
    </div>
    <div class="route">
      <div class="route-label">E-MAIL</div>
      <p class="mail">sales@aoba-suiri.example</p>
    </div>
    <div class="route">
      <div class="route-label">FAX</div>
      <p class="tel">0120-000-222<small>裏面の注文シートをご利用ください</small></p>
    </div>
  </section>

  <aside class="oem">
    <h3 class="oem-title">御社オリジナルの精製水を<br>ご販売されませんか?</h3>
    <div class="oem-badge">OEM<br>製造・販売<br>承ります</div>
    <p class="oem-text">OEM製品のデザインに御社の名前を入れて、オリジナル商品として製造いたします。</p>
    <ul class="oem-points">
      <li>御社のデザインを印刷したオリジナルパッケージを製作</li>
      <li>小ロットからご相談ください</li>
      <li>詳しくはお電話またはメールで</li>
    </ul>
  </aside>

  <footer class="contact">
    <span class="contact-tag">お問い合わせ</span>
    <p class="company">株式会社 青葉 <small>(アクア通販)</small></p>
    <p class="contact-num"><span><small>TEL</small>0900-00-1234</span><span><small>FAX</small>0900-00-1234</span></p>
  </footer>

  <div class="fax-band">FAXでのご注文は、<b>裏面の注文シート(FAX専用)</b>をご利用ください。</div>
</div>
</body>
</html>
```